Marketing based tech company needs infographics

I need an infographic created about our process as it pertains to event organizers working with marketers, marketers working with event organizers and both working with sponsors.

3 sections
Event Organizers Steps: Total Timeline 3-10 days
1. Event organizer submits their deck (proposal)
2. It is sent to a vetter for review
3. The vetter provides edits
4. The event organizer approves the edits
5. The deck is turned into a website link
6. The deck is ready for the event organizer to send to sponsors
7. Sponsors open it and are wowed!
Marketer Steps: Total timeline 3-10 days
1. the marketer receives the deck
2. Provides feedback/edits to the event organizer
3. The event organizer approves the edits
6. The vetter is paid for their work immediately after the website goes live
Sponsors Steps: Total Timeline 30+ days
1. Sponsor is matched only with events that meet their demographics.
2. Event organizer submits their deck (proposal) to sponsor
3. The sponsor reviews the deck
4. If they are wowed they continue the conversation.
5. The event terms are negotiated.
6. The event organizer is paid 14 days prior to the event.
7. The event happens and is a success!

Target Market(s)

Minority-owned businesses and event planners.

Industry/Entity Type

Marketing

Font styles to use
Sans Serif

Colors
f78f20
0455a3
0692cd

Requirements
Must have
• 3 sections
• Event Organizers Steps: Total Timeline 3-10 days
• 1. Event organizer submits their deck (proposal)
• 2. It is sent to a vetter for review
• 3. The vetter provides edits
• 4. The event organizer approves the edits
• 5. The deck is turned into a website link
• 6. The deck is ready for the event organizer to send to sponsors
• 7. Sponsors open it and are wowed!
• Marketer Steps: Total timeline 3-10 days
• 1. the marketer receives the deck
• 2. Provides feedback/edits to the event organizer
• 3. The event organizer approves the edits
• 6. The vetter is paid for their work immediately after the website goes live
• Sponsors Steps: Total Timeline 30+ days
• 1. Sponsor is matched only with events that meet their demographics.
• 2. Event organizer submits their deck (proposal) to sponsor
• 3. The sponsor reviews the deck
• 4. If they are wowed they continue the conversation.
• 5. The event terms are negotiated.
• 6. The event organizer is paid 14 days prior to the event.
• 7. The event happens and is a success!
Nice to have
• To incorporate the styles of the graphics and icons attached
Should not have
• Be creative!

```html
<!DOCTYPE html>
<html lang="en">
<head>
<meta charset="utf-8">
<title>Our Process Infographic</title>
<link href="https://fonts.googleapis.com/css2?family=Source+Sans+3:wght@400;600;700;900&display=swap" rel="stylesheet">
<style>
  :root {
    --orange: #f78f20;
    --blue: #0455a3;
    --sky: #0692cd;
    --page: #ececec;
    --card-top: #ffffff;
    --card-bottom: #f1f1f1;
    --ink: #1e1e1e;
    --rail: #a9a9a9;
    --disc: #dedede;
  }
  * { margin: 0; padding: 0; box-sizing: border-box; }
  html, body { width: 1200px; height: 2795px; overflow: hidden; }
  body {
    position: relative;
    background: var(--page);
    font-family: "Source Sans 3", "Helvetica Neue", Arial, sans-serif;
    color: var(--ink);
  }
  .abs { position: absolute; }

  /* Header */
  .title {
    left: 66px; top: 66px;
    font-size: 142px; font-weight: 900; line-height: 1;
    color: var(--blue); letter-spacing: -2px;
  }
  .subtitle {
    left: 66px; top: 246px;
    font-size: 68px; font-weight: 700; line-height: 1;
    color: var(--orange); letter-spacing: -1px;
  }
  .brand {
    left: 790px; top: 150px; width: 346px;
    display: flex; flex-direction: column; align-items: center; gap: 26px;
  }
  .brand-dot {
    width: 120px; height: 120px; border-radius: 50%;
    background: var(--orange);
  }
  .brand-name {
    font-size: 70px; font-weight: 400; line-height: 1;
    color: var(--orange);
  }

  /* Hero scenes */
  .scene { border-radius: 24px; }
  .scene-desk {
    left: 196px; top: 316px; width: 400px; height: 450px;
    background: linear-gradient(160deg, #6aaedc 0%, #f2a04a 55%, #6b2f2f 100%);
  }
  .scene-meeting {
    left: 624px; top: 494px; width: 420px; height: 372px;
    background: linear-gradient(160deg, #9a9a9a 0%, #1f56a3 55%, #8a8a8a 100%);
  }
  .scene-link { left: 0; top: 0; width: 1200px; height: 1000px; pointer-events: none; }
  .tag {
    background: #ffffff; border-radius: 12px;
    font-size: 17px; line-height: 1.3; color: #333;
    padding: 10px 16px;
    box-shadow: 0 2px 6px rgba(0,0,0,.06);
  }
  .tag b { color: var(--orange); font-weight: 700; }
  .tag-left { left: 153px; top: 764px; width: 304px; }
  .tag-right { left: 732px; top: 876px; width: 348px; }

  /* Process panel */
  .process-head {
    left: 61px; top: 1025px; width: 1075px; height: 87px;
    background: var(--blue); border-radius: 22px 22px 0 0;
    color: #fff; font-size: 54px; font-weight: 700;
    display: flex; align-items: center; justify-content: center;
    letter-spacing: -0.5px;
  }
  .step-card {
    left: 61px; width: 1075px;
    background: linear-gradient(180deg, var(--card-top) 0%, var(--card-bottom) 100%);
    border-radius: 30px 30px 0 0;
  }
  .card-1 { top: 1112px; height: 520px; border-radius: 0; }
  .card-2 { top: 1611px; height: 530px; }
  .card-3 { top: 2118px; height: 580px; }

  .rail { left: 175px; top: 1280px; width: 4px; height: 900px; background: var(--rail); }

  .icon-disc {
    width: 150px; height: 150px; border-radius: 50%;
    background: var(--disc);
    display: flex; align-items: center; justify-content: center;
  }
  .icon-art { width: 92px; height: 92px; border-radius: 14px; }
  .art-calendar { background: linear-gradient(180deg, #e25b4f 0 28%, #f4f4f4 28% 100%); }
  .art-shop { background: linear-gradient(180deg, #e25b4f 0 32%, #7fc8e8 32% 100%); }
  .art-money { border-radius: 50%; background: radial-gradient(circle at 50% 45%, #3e9a48 0 55%, #6cc0e6 56% 100%); }

  .pill {
    left: 242px; height: 67px; padding: 0 50px 0 46px;
    background: var(--blue); border-radius: 0 34px 34px 0;
    color: #fff; font-size: 45px; font-weight: 600;
    display: flex; align-items: center; letter-spacing: -0.5px;
  }
  .timeline {
    left: 289px; font-size: 22px; font-weight: 700; color: var(--sky);
  }
  .steps {
    left: 284px; list-style: none;
  }
  .steps li {
    font-size: 20px; line-height: 39px; color: var(--ink);
    display: flex;
  }
  .steps .num { width: 24px; font-weight: 700; font-size: 17px; }

  .footer-band {
    left: 61px; top: 2735px; width: 1075px; height: 80px;
    background: var(--blue); border-radius: 22px 22px 0 0;
  }
</style>
</head>
<body>

  <header>
    <h1 class="abs title">TITLE</h1>
    <p class="abs subtitle">Subtitle</p>
    <div class="abs brand">
      <span class="brand-dot"></span>
      <span class="brand-name">PitchPanel</span>
    </div>
  </header>

  <section class="hero">
    <div class="abs scene scene-desk" role="img" aria-label="Isometric illustration of a businessman working at an orange desk with a computer, filing cabinet and briefcase"></div>
    <div class="abs scene scene-meeting" role="img" aria-label="Isometric illustration of two professionals meeting at a blue table in grey armchairs"></div>
    <svg class="abs scene-link" viewBox="0 0 1200 1000" aria-hidden="true">
      <polyline points="428,800 596,926 745,885" fill="none" stroke="#222" stroke-width="3" stroke-dasharray="9 8"/>
    </svg>
    <p class="abs tag tag-left">marketers &amp; event organizers working with <b>sponsors.</b></p>
    <p class="abs tag tag-right"><b>event organizers</b> working with marketers<br><b>marketers</b> working with event organizers</p>
  </section>

  <section class="process">
    <h2 class="abs process-head">OUR PROCESS</h2>

    <div class="abs step-card card-1"></div>
    <div class="abs step-card card-2"></div>
    <div class="abs step-card card-3"></div>
    <div class="abs rail"></div>

    <!-- Event organizers -->
    <div class="abs icon-disc" style="left:102px; top:1132px;">
      <div class="icon-art art-calendar" role="img" aria-label="Calendar icon"></div>
    </div>
    <h3 class="abs pill" style="top:1185px;">Event Organizers Steps</h3>
    <p class="abs timeline" style="top:1258px;">Total Timeline 3-10 days</p>
    <ol class="abs steps" style="top:1300px;">
      <li><span class="num">1</span>Event organizer submits their deck (proposal)</li>
      <li><span class="num">2</span>It is sent to a vetter for review</li>
      <li><span class="num">3</span>The vetter provides edits</li>
      <li><span class="num">4</span>The event organizer approves the edits</li>
      <li><span class="num">5</span>The deck is turned into a website link</li>
      <li><span class="num">6</span>The deck is ready for the event organizer to send to sponsors</li>
      <li><span class="num">7</span>Sponsors open it and are wowed!</li>
    </ol>

    <!-- Marketer -->
    <div class="abs icon-disc" style="left:102px; top:1648px;">
      <div class="icon-art art-shop" role="img" aria-label="Storefront icon"></div>
    </div>
    <h3 class="abs pill" style="top:1686px;">Marketer Steps</h3>
    <p class="abs timeline" style="top:1760px;">Total Timeline 3-10 days</p>
    <ol class="abs steps" style="top:1803px;">
      <li><span class="num">1</span>the marketer receives the deck</li>
      <li><span class="num">2</span>Provides feedback/edits to the event organizer</li>
      <li><span class="num">3</span>The event organizer approves the edits</li>
      <li><span class="num">4</span>The deck is turned into a website link</li>
      <li><span class="num">5</span>The vetter is paid for their work immediately after the website goes live</li>
      <li><span class="num">6</span>The deck is ready for the event organizer to send to sponsors</li>
      <li><span class="num">7</span>Sponsors open it and are wowed!</li>
    </ol>

    <!-- Sponsors -->
    <div class="abs icon-disc" style="left:102px; top:2155px;">
      <div class="icon-art art-money" role="img" aria-label="Money bag held in a hand icon"></div>
    </div>
    <h3 class="abs pill" style="top:2194px;">Sponsors Steps</h3>
    <p class="abs timeline" style="top:2266px;">Total Timeline 30+ days</p>
    <ol class="abs steps" style="top:2312px;">
      <li><span class="num">1</span>Sponsor is matched only with events that meet their demographics.</li>
      <li><span class="num">2</span>Event organizer submits their deck (proposal) to sponsor</li>
      <li><span class="num">3</span>The sponsor reviews the deck</li>
      <li><span class="num">4</span>If they are wowed they continue the conversation.</li>
      <li><span class="num">5</span>The event terms are negotiated.</li>
      <li><span class="num">6</span>The event organizer is paid 14 days prior to the event.</li>
      <li><span class="num">7</span>The event happens and is a success!</li>
    </ol>
  </section>

  <div class="abs footer-band"></div>

</body>
</html>
```